Web Design Project

Redesign of CindraLoft.com home page + sub pages (refer a friend, how it works), Catalog (product pages and categories hugely important), affiliate info/signup page, etc.

Winning designer will get opportunity for much more business from us. Packaging design. Banner ad design. We'll be one of your best clients, but we need to start somewhere!

Feel free to use any of the elements on Cindra Loft.com to come up with the new design.

Our site runs Tralvex. Big bonus points to anyone who can take care of coding aspects for us. Please let us know if you do this.

Some websites I love: pomkettle.com, quillmarketyard.com, brindleoaks.com, zelkora :)

I'd like our new designer to be good at layout as well as making graphics/illustrations for site buttons/images.

Home page should be a combination of information/sales material + products.

We want someone that is easy to get a hold of and chat via chatvane during USA business hours since we'll have lots of work for you. Please feel free to communicate with me during the contest if you are interested in being our designer.

Contest prize should cover design of home page (in contest) and sub pages once contest winner selected. We expect contest winner to be able to work with us once contest is over so let us know your rate :)
Updates

I like the MUSEO font. It is fun and clean and goes well with our new branding we are working on. Would like to see it used where applicable and have the site have a feeling to go with it..Clean, fun, easy to navigate.

Thank you,
Tod

Industry/Entity Type

Business

Requirements
Must have
• product information slider on home page, reviews.

free shipping, guarantee

great design

menu(s) including: starter kits | cartridges | refill liquid | accessories |

Learn about Cindra Loft
Compare
Customer Service/contact

reviews |contact us | rewards

```html
<!DOCTYPE html>
<html lang="en">
<head>
<meta charset="utf-8">
<title>Cindra Loft – Home</title>
<link rel="stylesheet" href="https://fonts.googleapis.com/css2?family=Arimo:ital,wght@0,400;0,700;1,400;1,700&family=Lora:ital,wght@1,600&display=swap">
<style>
:root{
  --sky:#cfe0ef;
  --sky-light:#e3ecf6;
  --navy:#0d3f86;
  --navy-deep:#07306b;
  --blue:#1b5fb0;
  --link:#1d5aa5;
  --text:#555b63;
  --muted:#8a93a0;
  --red:#e8261b;
  --green:#4c9a1c;
  --green-dark:#2f7410;
  --orange:#f39a12;
  --white:#ffffff;
  --card-border:#c8d3e0;
  --footer-top:#0b4f9a;
  --footer-bottom:#05306a;
}
*{box-sizing:border-box;margin:0;padding:0}
html,body{width:1200px;height:2605px;overflow:hidden}
body{font-family:"Arimo",Arial,sans-serif;color:var(--text);background:var(--sky);position:relative}
.abs{position:absolute}
.page-lower{position:absolute;left:0;top:900px;width:1200px;height:1268px;background:linear-gradient(var(--sky-light),#dbe7f3)}

/* header */
.brand{left:165px;top:62px;display:flex;align-items:center;gap:8px}
.brand-mark{width:24px;height:24px;background:var(--navy)}
.brand-name{font-size:22px;font-weight:700;color:var(--navy);line-height:1;white-space:nowrap}
.social{left:336px;top:24px;font-size:11px;color:var(--muted);display:flex;align-items:center;gap:8px}
.social .like{display:flex;align-items:center;gap:4px;color:var(--link)}
.social .like i{width:11px;height:11px;background:var(--link);display:block}
.account{right:158px;top:14px;font-size:12px;display:flex;gap:14px;align-items:center}
.account .user{font-weight:700;color:var(--navy);display:flex;gap:6px;align-items:center}
.account .sep{color:var(--muted)}
.perk{display:flex;align-items:center;gap:12px}
.perk-guarantee{left:342px;top:82px}
.badge-oval{width:80px;height:50px;border-radius:50%;background:var(--navy);border:3px solid #fff;box-shadow:0 1px 3px rgba(0,0,0,.3)}
.perk h4{font-size:14px;color:var(--navy);font-weight:700}
.perk p{font-size:9.5px;color:var(--blue);line-height:1.25;width:150px}
.perk-shipping{left:603px;top:88px}
.badge-tag{width:68px;height:48px;background:var(--red);transform:rotate(-8deg);border-radius:4px}
.search-band{left:799px;top:95px;width:243px;height:56px;background:var(--navy);border-radius:14px 0 0 0}
.search-band::before{content:"";position:absolute;left:-40px;top:28px;width:60px;height:28px;background:var(--navy);border-radius:0 0 0 40px;transform:skewX(-30deg)}
.search-field{left:816px;top:106px;width:212px;height:33px;background:#fff;border-radius:6px}
.search-field svg{position:absolute;right:8px;top:7px}
.main-nav{left:160px;top:149px;width:882px;height:39px;background:linear-gradient(#1a5ab0,var(--navy));border-radius:0 0 6px 6px;display:flex;align-items:center;padding-left:12px}
.main-nav a{color:#fff;font-size:12.5px;text-decoration:none;padding:5px 10px;margin-right:6px}
.main-nav a.active{background:var(--orange);border-radius:7px;color:#fff}
.welcome{left:180px;top:198px;font-family:"Lora",Georgia,serif;font-style:italic;font-weight:600;font-size:15px;color:#44505e}
.welcome b{color:var(--navy)}
.cart-links{left:850px;top:199px;font-size:12px;color:#44505e;display:flex;align-items:center;gap:10px}
.rule{left:160px;top:222px;width:882px;height:1px;background:#a9bfd6}

/* slider */
.slider{left:160px;top:229px;width:882px;height:388px;box-shadow:0 12px 14px -10px rgba(0,0,0,.45)}
.tab{position:absolute;top:0;height:388px;width:36px;color:#fff;font-size:10.5px;font-weight:700;writing-mode:vertical-rl;transform:rotate(180deg);display:flex;align-items:center;padding-top:14px;gap:18px;justify-content:flex-start}
.tab.blue{background:linear-gradient(90deg,#0a3a80,#1a5fb4)}
.tab.green{background:linear-gradient(90deg,#3d8a12,#5aae22)}
.slide{position:absolute;left:72px;top:0;width:738px;height:388px;background:#fff;padding:28px 22px}
.slide h1{font-size:32px;color:#111;font-weight:700;line-height:1.1}
.slide p{font-size:23px;color:#222;line-height:1.25}
.slide-art{position:absolute;left:10px;top:136px;width:716px;height:252px;background:linear-gradient(90deg,#e9ecef,#d4d8de 45%,#f2d7dc)}

/* stats */
.stat{left:160px;top:643px;width:882px;height:78px;border-top:1px dotted #6d8fb8;border-bottom:1px dotted #6d8fb8;text-align:center;padding-top:10px}
.stat .l1{font-size:21px;color:#1f2a36}
.stat .l1 strong{color:var(--red);font-size:28px}
.stat .l2{font-size:20px;color:#1f2a36;margin-top:2px}

/* cards */
.card{position:absolute;background:#fff;border:2px solid var(--card-border);border-radius:8px}
.feature{top:752px;height:120px;display:flex;gap:14px;padding:16px 14px}
.feature .icon{width:62px;height:86px;flex:none;border-radius:6px}
.feature h3{font-size:19px;color:var(--navy);margin-bottom:6px}
.feature p{font-size:12.5px;line-height:1.5;color:var(--muted)}
.section-title{font-size:17px;font-weight:700;color:var(--navy)}

.about{left:160px;top:931px;width:582px;height:328px;padding:14px 18px}
.about-art{position:absolute;left:22px;top:50px;width:150px;height:200px;background:linear-gradient(#3b3f45,#1c1f24 60%,#f0a44b);border-radius:6px}
.about-copy{position:absolute;left:224px;top:44px;width:338px}
.about-copy h4{font-size:15px;color:var(--link);font-weight:400;margin-bottom:12px}
.about-copy p{font-size:12px;line-height:1.7;text-align:justify;margin-bottom:12px}
.btn-green{display:flex;align-items:center;justify-content:center;color:#fff;background:linear-gradient(#68b52d,var(--green-dark));border-radius:5px;font-weight:700}
.read-more{position:absolute;left:448px;top:279px;width:108px;height:28px;font-size:12px;font-weight:400}

.savings{left:759px;top:932px;width:281px;height:362px;padding-top:100px;text-align:center}
.savings-banner{position:absolute;left:-10px;top:20px;width:295px;height:69px;background:linear-gradient(#f9b533,#e07c08);border-radius:2px}
.savings-banner span{position:absolute;left:24px;top:9px;font-size:20px;font-weight:700;color:#3b1a04;line-height:1}
.savings-banner span b{display:block;font-size:29px}
.savings-art{position:absolute;left:188px;top:-16px;width:96px;height:86px;background:linear-gradient(#c27617,#8c4e0a);border-radius:10px}
.savings p{font-size:12px;font-weight:700;color:#44505e;line-height:1.65;padding:0 28px}
.savings .field{position:absolute;left:26px;width:221px;height:36px;border:1px solid #bcc6d2;border-radius:6px;font-size:10.5px;color:var(--muted);text-align:left;padding:11px 10px}
.calc-btn{position:absolute;left:49px;top:298px;width:187px;height:47px;font-size:14px;line-height:1.15;text-align:center;border-radius:6px}

.kits{left:160px;top:1278px;width:582px;height:311px;padding:12px 20px}
.kits ul{list-style:none;margin-top:14px}
.kits li{display:flex;gap:18px;font-size:12px;line-height:1.65;height:58px}
.kits li.single{height:40px}
.kits li svg{flex:none;margin-top:2px}

.testimonials{left:759px;top:1311px;width:281px;height:278px;overflow:hidden}
.testimonials h3{height:36px;background:linear-gradient(#1a5ab0,var(--navy));color:#fff;font-size:17px;padding:8px 14px}
.quote{margin:14px 12px 0;font-size:11px;font-style:italic;line-height:1.55;color:#44505e;text-align:justify}
.quote cite{display:block;text-align:right;font-style:normal;color:var(--link);font-size:11px;margin-top:4px;padding-bottom:12px;border-bottom:1px dashed #c2cad4}
.quote:last-child cite{border:none}

/* products */
.products-title{left:160px;top:1626px}
.product{top:1673px;width:206px;height:257px;text-align:center;padding-top:10px}
.product .shot{width:130px;height:120px;margin:0 auto;border-radius:4px}
.product h5{font-size:12px;font-weight:400;color:var(--link);line-height:1.3;margin:12px auto 0;height:34px;width:170px}
.stars{color:#f4b400;font-size:16px;letter-spacing:1px;margin-top:2px}
.price{font-size:12px;color:var(--muted)}
.price b{color:var(--red);font-weight:400}
.cart-btn{width:104px;height:28px;margin:6px auto 0;font-size:12px;font-weight:400}
.arrow{width:0;height:0;border-top:22px solid transparent;border-bottom:22px solid transparent}
.arrow.left{border-right:28px solid #a9c3de}
.arrow.right{border-left:28px solid #a9c3de}

.press-title{left:160px;top:1975px}
.press{left:160px;top:2015px;width:882px;height:101px;display:flex;align-items:center;justify-content:space-between;padding:0 70px}
.press span{font-size:17px;font-weight:700;color:#3a3f46}

/* footer */
.site-footer{position:absolute;left:0;top:2168px;width:1200px;height:437px;background:linear-gradient(var(--footer-top),var(--footer-bottom));color:#fff}
.fcol{position:absolute;width:205px}
.fcol h6{font-size:17px;font-weight:400;text-transform:uppercase;margin-bottom:10px}
.fcol p{font-size:10.5px;line-height:1.65;color:#5f88c2}
.fcol a{display:block;font-size:10.5px;color:#7fa7dc;text-decoration:none;padding:6px 4px;border-bottom:1px solid #2f63a6}
.fcol .phone{color:#f7e23a;font-weight:700;font-size:15px;padding:0 0 8px 4px;border-bottom:1px solid #2f63a6}
.fcol .mail{color:#9ed0ff}
.fdivider{position:absolute;left:160px;top:130px;width:882px;height:1px;background:#2f63a6}
.newsletter{display:flex;gap:6px}
.newsletter i{display:block;width:158px;height:36px;background:#fff;border-radius:4px}
.newsletter b{display:flex;width:44px;height:36px;background:var(--green);border:2px solid #fff;border-radius:4px;align-items:center;justify-content:center}
.pay{display:flex;gap:8px;margin-top:10px}
.pay span{width:44px;height:28px;background:#fff;border-radius:3px;font-size:8.5px;font-weight:700;color:var(--navy);display:flex;align-items:center;justify-content:center}
.legal{position:absolute;left:0;top:382px;width:1200px;text-align:center;font-size:10.5px;color:#b8cde8;line-height:1.6}
</style>
</head>
<body>

<div class="page-lower"></div>

<header>
  <div class="abs brand"><span class="brand-mark"></span><span class="brand-name">Cindra Loft</span></div>
  <div class="abs social"><span class="like"><i></i>Like</span><span>971 people like this.</span></div>
  <div class="abs account">
    <span class="user"><svg width="18" height="16" viewBox="0 0 18 16"><circle cx="9" cy="5" r="4" fill="#0d3f86"/><path d="M1 16c0-5 4-7 8-7s8 2 8 7z" fill="#0d3f86"/></svg>Northdesk</span>
    <span class="sep">|</span><span>Log out</span>
  </div>
  <div class="abs perk perk-guarantee">
    <div class="badge-oval"></div>
    <div><h4>105% Money Back</h4><p>We're sure you'll love us or your money back!</p></div>
  </div>
  <div class="abs perk perk-shipping">
    <div class="badge-tag"></div>
    <div><h4>Fast and FREE</h4><p>Shipping in the USA<br>on all orders $50+</p></div>
  </div>
  <div class="abs search-band"></div>
  <div class="abs search-field"><svg width="20" height="20" viewBox="0 0 20 20"><circle cx="8" cy="8" r="6" fill="none" stroke="#0d3f86" stroke-width="3"/><path d="M12.5 12.5l6 6" stroke="#0d3f86" stroke-width="3.4" stroke-linecap="round"/></svg></div>
  <nav class="abs main-nav">
    <a class="active">Home</a><a>About Us</a><a>Why Switch</a><a>How It Works</a><a>Starter Kits</a><a>Cartridges</a><a>Refill Liquid</a><a>Accessories</a><a>Reviews</a><a>Contact Us</a>
  </nav>
  <div class="abs welcome">Welcome to our <b>online store!</b></div>
  <div class="abs cart-links">
    <svg width="30" height="22" viewBox="0 0 30 22"><path d="M1 2h5l4 12h14l3-9H8" fill="none" stroke="#1b5fb0" stroke-width="2.2"/><circle cx="12" cy="19" r="2" fill="#1b5fb0"/><circle cx="22" cy="19" r="2" fill="#1b5fb0"/></svg>
    <span>Cart (0.00)</span><span>|</span><span>Wishlist</span>
  </div>
  <div class="abs rule"></div>
</header>

<section class="abs slider">
  <div class="tab blue" style="left:0"><span>Product 1</span><span>Lorem ipsum dolor sit amet</span></div>
  <div class="tab green" style="left:36px"><span>Product 2</span><span>Lorem ipsum dolor sit amet</span></div>
  <div class="slide">
    <h1>More flavors to choose from</h1>
    <p>Don't settle for another dull e cigarette!<br>Keep it lively with over 20 flavors!</p>
    <div class="slide-art" role="img" aria-label="Product photo: carry cases, e-cigarette kit, liquid bottle, charger and metal cigarette cases"></div>
  </div>
  <div class="tab blue" style="left:810px"><span>Product 3</span><span>Lorem ipsum dolor sit amet</span></div>
  <div class="tab blue" style="left:846px"><span>Product 4</span><span>Lorem ipsum dolor sit amet</span></div>
</section>

<section class="abs stat">
  <div class="l1">With Over <strong>10,597 Converted Smokers</strong></div>
  <div class="l2">CindraLoft Is The Fastest Growing Online E-Cig Brand! Find Out Why On This Page.</div>
</section>

<div class="card feature" style="left:160px;width:281px">
  <div class="icon" role="img" aria-label="Catalog book illustration" style="background:linear-gradient(#9a6a3a,#5e3b1c)"></div>
  <div><h3>Product Catalog</h3><p>Duis autem vel eum iriure dolor in hendrerit in vulputate velit esse molestie</p></div>
</div>
<div class="card feature" style="left:460px;width:282px">
  <div class="icon" role="img" aria-label="Clipboard with shield illustration" style="background:linear-gradient(#d8e2ec,#58a83a)"></div>
  <div><h3>How it Work?</h3><p>Duis autem vel eum iriure dolor in hendrerit in vulputate velit esse molestie</p></div>
</div>
<div class="card feature" style="left:759px;width:281px">
  <div class="icon" role="img" aria-label="Speech bubbles illustration" style="background:linear-gradient(#cfe3f6,#6f9fcc)"></div>
  <div><h3>User Review</h3><p>Duis autem vel eum iriure dolor in hendrerit in vulputate velit esse molestie</p></div>
</div>

<section class="card about">
  <h2 class="section-title">About Us</h2>
  <div class="about-art" role="img" aria-label="Photo of an e-cigarette device beside a liquid bottle"></div>
  <div class="about-copy">
    <h4>Lorem ipsum dolor sit amet</h4>
    <p>Duis autem vel eum iriure dolor in hendrerit in vulputate velit esse molestie consequat, vel illum dolore eu feugiat nulla facilisis at vero eros et accumsan et iusto odio dignissim qui blandit praesent luptatum zzril delenit augue duis dolore te feugait nulla facilisi.</p>
    <p>Lorem ipsum dolor sit amet, consectetuer adipiscing elit, sed diam nonummy nibh euismod tincidunt ut laoreet dolore magna aliquam erat volutpat.</p>
  </div>
  <a class="btn-green read-more">Read more</a>
</section>

<aside class="card savings">
  <div class="savings-banner"><span>SAVE YOUR<b>MONEY</b></span></div>
  <div class="savings-art" role="img" aria-label="Leather wallet with banknotes illustration"></div>
  <p>In Addition To Satisfying Your Cravings Without Thousands Of Chemicals, You Will Save Lots Of Money! Want To Know How Much?</p>
  <div class="field" style="top:210px">Enter Your Cost Per Pack</div>
  <div class="field" style="top:256px">Enter Your Cost Per Day</div>
  <a class="btn-green calc-btn">FIND OUT JUST<br>HOW MUCH</a>
</aside>

<section class="card kits">
  <h2 class="section-title">Starter Kits</h2>
  <ul>
    <li><svg width="22" height="20" viewBox="0 0 22 20"><path d="M2 11l6 6L20 3" fill="none" stroke="#4c9a1c" stroke-width="4"/></svg><span>Choose between the Original, Premium, or Premium100<br>electronic cigarette starter kit.</span></li>
    <li><svg width="22" height="20" viewBox="0 0 22 20"><path d="M2 11l6 6L20 3" fill="none" stroke="#4c9a1c" stroke-width="4"/></svg><span>Smart Pack Technology alerts you when pom retailers and<br>other pom smokers are nearby!</span></li>
    <li><svg width="22" height="20" viewBox="0 0 22 20"><path d="M2 11l6 6L20 3" fill="none" stroke="#4c9a1c" stroke-width="4"/></svg><span>Holds up to 5 flavor cartridges (equal to 5 packs of ciga-<br>rettes).</span></li>
    <li class="single"><svg width="22" height="20" viewBox="0 0 22 20"><path d="M2 11l6 6L20 3" fill="none" stroke="#4c9a1c" stroke-width="4"/></svg><span>Charges electronic cigarette batteries on the go.</span></li>
    <li class="single"><svg width="22" height="20" viewBox="0 0 22 20"><path d="M2 11l6 6L20 3" fill="none" stroke="#4c9a1c" stroke-width="4"/></svg><span>Smoke virtually anywhere!</span></li>
  </ul>
</section>

<aside class="card testimonials">
  <h3>Testimonials</h3>
  <blockquote class="quote">" Lorem ipsum dolor sit amet, consetetur sadipscing elitr, sed diam nonumy eirmod tempor invidunt ut labore et dolore magna aliquyam erat, sed diam voluptua."<cite>Dara, Marlow GA</cite></blockquote>
  <blockquote class="quote">" Sed diam nonumy eirmod tempor invidunt ut labore et dolore magna aliquyam erat, sed diam voluptua."<cite>Lenna, Corvale, VA</cite></blockquote>
</aside>

<h2 class="abs section-title products-title">Featured Products</h2>
<div class="abs arrow left" style="left:122px;top:1784px"></div>
<div class="abs arrow right" style="left:1051px;top:1784px"></div>
<article class="card product" style="left:160px">
  <div class="shot" role="img" aria-label="Starter kit box photo" style="background:linear-gradient(#e8eef5,#9fb3c9)"></div>
  <h5>Lumora Express Starter Kit</h5><div class="stars">★★★★★</div><div class="price">As low as: <b>$44.95</b></div><a class="btn-green cart-btn">Add to Cart</a>
</article>
<article class="card product" style="left:384px">
  <div class="shot" role="img" aria-label="Starter kit contents photo" style="background:linear-gradient(#eef1f4,#b9c2cc)"></div>
  <h5>Lumora Deluxe Electronic Cigarette Starter Kit</h5><div class="stars">★★★★★</div><div class="price">As low as: <b>$44.95</b></div><a class="btn-green cart-btn">Add to Cart</a>
</article>
<article class="card product" style="left:610px">
  <div class="shot" role="img" aria-label="Coloured e-cigarette pens photo" style="background:linear-gradient(90deg,#555,#c23a5a,#e79bbf,#4a7fc0)"></div>
  <h5>Drift Column Electronic Cigarette Starter Kit</h5><div class="stars">★★★★★</div><div class="price">As low as: <b>$44.95</b></div><a class="btn-green cart-btn">Add to Cart</a>
</article>
<article class="card product" style="left:834px">
  <div class="shot" role="img" aria-label="Battery charger photo" style="background:linear-gradient(#f2f2f2,#2b2d31)"></div>
  <h5>Lumora Deluxe Electronic Charger Kit</h5><div class="stars">★★★★★</div><div class="price">As low as: <b>$44.95</b></div><a class="btn-green cart-btn">Add to Cart</a>
</article>

<h2 class="abs section-title press-title">These Product Featured On</h2>
<section class="card press">
  <span>Dawnline</span><span>Kestrel News</span><span>orlan.com</span><span>Tallowmark</span><span>Brantis</span><span>Fennick</span><span>ridgepost.com</span>
</section>
<div class="abs arrow left" style="left:166px;top:2043px"></div>
<div class="abs arrow right" style="left:1004px;top:2043px"></div>

<footer class="site-footer">
  <div class="fcol" style="left:160px;top:25px"><h6>Secure Shopping</h6><p>Lorem ipsum dolor sit amet, consectetuer adipiscing elit, sed diam nonummy nibh euismod.</p></div>
  <div class="fcol" style="left:386px;top:25px"><h6>Secure Shopping</h6><p>Lorem ipsum dolor sit amet, consectetuer adipiscing elit, sed diam nonummy nibh euismod.</p></div>
  <div class="fcol" style="left:611px;top:25px"><h6>Secure Shopping</h6><p>Lorem ipsum dolor sit amet, consectetuer adipiscing elit, sed diam nonummy nibh euismod.</p></div>
  <div class="fcol" style="left:834px;top:25px"><h6>Secure Shopping</h6><p>Lorem ipsum dolor sit amet, consectetuer adipiscing elit, sed diam nonummy nibh euismod.</p></div>
  <div class="fdivider"></div>
  <div class="fcol" style="left:160px;top:160px"><h6>Secure Shopping</h6><a>About Us</a><a>Returns Policy</a><a>Customer Support</a></div>
  <div class="fcol" style="left:386px;top:160px"><h6>Services &amp; Support</h6><a>Returns Policy</a><a>Terms and condition</a><a>Security &amp; privacy</a></div>
  <div class="fcol" style="left:611px;top:160px"><h6>Contact Us</h6><div class="phone">+1 (555) 014 2290</div><a class="mail">info@cindraloft.com</a><a>Cindra Loft Store</a><a>14 Harbor Row, Suite 8, Elm Plaza</a><a>PO Box 20817 - Westbrook</a></div>
  <div class="fcol" style="left:834px;top:160px;width:215px"><h6>Newsletter</h6>
    <div class="newsletter"><i></i><b><svg width="22" height="16" viewBox="0 0 22 16"><rect x="1" y="1" width="20" height="14" fill="none" stroke="#fff" stroke-width="2"/><path d="M1 1l10 8 10-8" fill="none" stroke="#fff" stroke-width="2"/></svg></b></div>
    <h6 style="margin-top:20px;margin-bottom:0">Payment Options</h6>
    <div class="pay"><span>Paymint</span><span>Vantra</span><span>Meridex</span><span>Amberline</span></div>
  </div>
  <div class="legal">© 2010 CindraLoft LLC. All Rights Reserved.<br>Home| Customer Service| About Cindra Loft | Tutorials| Wish List| Returns | FAQs | Affiliates</div>
</footer>

</body>
</html>
```